Drug safety monitoring company requires a new corporate website

We are an outsourcing partner to large and small companies within the pharmaceutical industry. Our current website www.quorvanta.co.uk has not been updated in a long time. We want a new web site that is responsive and modern but with a clearly corporate and professional feel. We want a design based on a 12 column grid system (mobile and desktop version). We want to use a new, modern font (not the standard web fonts) - we will purchase as required. Content can be used as is from the current website. Red and white are the corporate colours, so a palate should be developed to match. We do not need as much red as is in the current website. New icons (preferably in svg format) would be great. We can also purchase new images from Framly (or other) as required. We would prefer submissions in Sketch if possible.

Target Market(s)

Pharmaceutical companies

Number of Pages Required

1 page

Font styles to use
Sans Serif

Colors
ec1f27
ffffff

Requirements
Must have
• Design based on 12 column grid system.
Responsive design (i.e. require a mobile and desktop version).
How should the menu look between desktop and mobile?
A coherent colour palete.
Content to come from the existing website: www.quorvanta.co.uk
How should links be styled?
How should headings, sub-headings, paragraphs be styled?
Nice to have
• Custom developed icons (these are along the bottom of the page on the existing website: Medical Information; Pharmacovigilance; Literature Monitoring; Training).
New imagery (the images on the current website are dated).
Submission ideally as Sketch files (but we are okay with photoshop too).
A new, modern, non-standard font.
Not so much red in the design.
If we had buttons on the website, how should they be styled?
If we had a form on the website, how should the fields be styled?

```html
<!DOCTYPE html>
<html lang="en">
<head>
<meta charset="utf-8">
<title>Quorvanta Pharmacovigilance</title>
<link href="https://fonts.googleapis.com/css2?family=Ubuntu:wght@400;500;700&display=swap" rel="stylesheet">
<style>
:root{
  --red:#ec1f27;
  --white:#ffffff;
  --hero:#3f3879;
  --footer:#1c1662;
  --ink:#2e2e33;
  --text:#3a3a40;
  --card-shadow:rgba(30,25,80,.12);
}
*{box-sizing:border-box;margin:0;padding:0}
html,body{width:928px;height:1200px;overflow:hidden}
body{font-family:"Ubuntu",sans-serif;background:var(--white);color:var(--text);position:relative}
.abs{position:absolute}

/* header + hero */
.hero{left:0;top:0;width:928px;height:401px;background:var(--hero);overflow:hidden}
.hero-photo{left:534px;top:47px;width:336px;height:336px;border-radius:50%;
  background:radial-gradient(circle at 55% 50%,rgba(60,90,200,.55) 0%,rgba(120,60,110,.35) 30%,rgba(80,75,150,.25) 55%,rgba(63,56,121,0) 72%)}
.brand{display:flex;align-items:center;gap:4px}
.brand-mark{width:9px;height:9px;border-radius:50%;background:var(--red)}
.brand-name{font-size:12px;font-weight:500;letter-spacing:2px;color:var(--white)}
.brand-sub{font-size:7px;color:var(--white);margin-top:2px;margin-left:13px}
.nav{top:34px;left:311px;display:flex;font-size:10px;color:var(--white)}
.nav a{color:var(--white);text-decoration:none;position:absolute;white-space:nowrap}
.nav .active::after{content:"";position:absolute;left:-3px;right:-3px;top:15px;height:1.5px;background:var(--red)}
.btn{background:var(--red);color:var(--white);border-radius:30px;display:flex;align-items:center;justify-content:center;text-decoration:none;font-weight:500;white-space:nowrap}
.nav-cta{left:714px;top:30px;width:102px;height:23px;font-size:10px;font-weight:400}
.hero-title{left:113px;top:154px;font-size:21px;line-height:28px;font-weight:700;color:var(--white);letter-spacing:.2px}
.hero-cta{left:113px;top:258px;width:133px;height:41px;font-size:10.5px;font-weight:700}
.hero-link{left:257px;top:272px;font-size:10px;color:var(--white)}
.scroll-down{left:452px;top:368px;width:23px;height:23px;border-radius:50%;background:var(--white)}

/* welcome */
.section-title{width:928px;left:0;text-align:center;font-size:21px;font-weight:700;color:var(--ink)}
.sub{font-size:10px;font-weight:700;color:var(--ink);line-height:14px}
.para{font-size:10px;line-height:14px;color:var(--text);width:350px}
.read{color:var(--red);text-decoration:none;display:block}

/* services */
.card{width:153px;height:169px;background:var(--white);box-shadow:0 1px 5px var(--card-shadow);text-align:center}
.card-icon{margin:7px auto 0;display:block}
.card-title{font-size:10.5px;font-weight:700;color:var(--red);margin-top:3px}
.card-text{font-size:8.6px;line-height:11px;color:var(--text);margin:18px auto 0;width:112px;height:54px}
.card-btn{width:103px;height:29px;margin:25px auto 0;font-size:10.5px;font-weight:700}

/* footer */
.footer{left:0;top:978px;width:928px;height:222px;background:var(--footer);color:var(--white)}
.foot-title{font-size:21px;font-weight:700;top:40px}
.foot-text{font-size:10px;top:84px;line-height:13px}
.social{top:116px;left:113px;display:flex;gap:7px}
.social span{width:17px;height:17px;border-radius:50%;background:rgba(255,255,255,.85)}
</style>
</head>
<body>

<header class="hero abs">
  <div class="hero-photo abs" role="img" aria-label="Photo of blue and red capsules and pills in a glass bowl"></div>

  <div class="abs" style="left:113px;top:33px">
    <div class="brand"><span class="brand-mark"></span><span class="brand-name">QUORVANTA</span></div>
    <div class="brand-sub">Pharmacovigilance</div>
  </div>

  <nav class="nav abs">
    <a class="active" style="left:0">Home</a>
    <a style="left:55px">About Us</a>
    <a style="left:127px">Qppv</a>
    <a style="left:180px">Our Services</a>
    <a style="left:268px">Contact Us</a>
    <a style="left:347px">Client</a>
  </nav>
  <a class="btn nav-cta abs">Get Started Now</a>

  <h1 class="hero-title abs">At Quorvanta we ansure that your business has<br>the best Pharmacovigilance support in the industry</h1>
  <a class="btn hero-cta abs">Get Started Now</a>
  <a class="hero-link abs" style="text-decoration:underline">Learn more</a>
  <div class="scroll-down abs">
    <svg width="23" height="23" viewBox="0 0 23 23"><path d="M8 10l3.5 3.5L15 10" fill="none" stroke="#ec1f27" stroke-width="1.6" stroke-linecap="round"/></svg>
  </div>
</header>

<main>
  <h2 class="section-title abs" style="top:441px">Welcome</h2>

  <h3 class="sub abs" style="left:113px;top:484px">Welcome to the Quorvanta<br>Pharmacovigilance</h3>
  <p class="para abs" style="left:113px;top:521px">We are an outsourcing partner to large and small companies within the pharmaceutical industry Our range of services is tailored to suit each of our client’s needs and cover both human and veterinary <a class="read">Read more...</a></p>

  <h3 class="sub abs" style="left:499px;top:498px">Pharmacovigilance</h3>
  <p class="para abs" style="left:500px;top:521px">is defined by WHO as ‘The science and activities relating to the detection, assessment, understanding and prevention of adverse effects or any other drug-related problems <a class="read">Read more...</a></p>

  <h3 class="sub abs" style="left:113px;top:593px">Our primary functions</h3>
  <p class="para abs" style="left:113px;top:616px">Our primary functions are EU QPPV and related pharmacovigilance services to assist and support Marketing Authorisation Holders (MAH), of pharmaceutical product licences, in their efforts to remain <a class="read">Read more...</a></p>

  <h3 class="sub abs" style="left:500px;top:593px">Good Pharmacovigilance Practice</h3>
  <p class="para abs" style="left:499px;top:616px">is dependant on a sound understanding of the key principles of this science and the ability to apply this knowledge competently on behalf of the client. <a class="read">Read more...</a></p>

  <h2 class="section-title abs" style="top:710px">Our Services</h2>

  <article class="card abs" style="left:113px;top:754px">
    <svg class="card-icon" width="18" height="16" viewBox="0 0 18 16" fill="none" stroke="#2e2e33" stroke-width=".9"><path d="M9 6.5L6.8 4.3a1.4 1.4 0 012-2L9 2.5l.2-.2a1.4 1.4 0 012 2z"/><path d="M2 10h2v5H2zM4 10.5h3.5l3 1h2.5l2.5-1.5v1.5l-3 2.5H4"/></svg>
    <h4 class="card-title">Medical Information</h4>
    <p class="card-text">Professional enquiry handling to support the safe and effective use of your products.</p>
    <a class="btn card-btn">Get started</a>
  </article>

  <article class="card abs" style="left:296px;top:754px">
    <svg class="card-icon" width="18" height="16" viewBox="0 0 18 16" fill="none" stroke="#2e2e33" stroke-width=".9"><path d="M9 15L2.5 8.5a3.6 3.6 0 015-5.2L9 4.6l1.5-1.3a3.6 3.6 0 015 5.2z"/><path d="M3 8h3l1.5-2.5 2 4 1.5-2h4"/></svg>
    <h4 class="card-title">Pharmacovigilance</h4>
    <p class="card-text">Ease the regulatory burden and keep compliant with current pharmacovigilance.</p>
    <a class="btn card-btn">Get started</a>
  </article>

  <article class="card abs" style="left:479px;top:754px">
    <svg class="card-icon" width="20" height="20" viewBox="0 0 20 20" fill="none" stroke="#2e2e33" stroke-width=".9"><rect x="1" y="1" width="15" height="12"/><path d="M3 10l3-4 3 2 4-5"/><circle cx="12" cy="13" r="3.3" fill="#fff"/><path d="M14.5 15.5L18 19"/></svg>
    <h4 class="card-title" style="margin-top:-1px">Literature Monitoring</h4>
    <p class="card-text" style="width:118px">Product safety through surveillance of published articles and case reports.</p>
    <a class="btn card-btn">Get started</a>
  </article>

  <article class="card abs" style="left:662px;top:754px">
    <svg class="card-icon" width="20" height="18" viewBox="0 0 20 18" fill="none" stroke="#2e2e33" stroke-width=".9"><rect x="1" y="1" width="18" height="12"/><path d="M7 17h6M10 13v4M5 6l5-2.5L15 6l-5 2.5z"/><path d="M7 7.2v2.3c2 1.3 4 1.3 6 0V7.2"/></svg>
    <h4 class="card-title">Training</h4>
    <p class="card-text">Professional enquiry handling to support the safe and effective use of your products.</p>
    <a class="btn card-btn">Get started</a>
  </article>
</main>

<footer class="footer abs">
  <h2 class="foot-title abs" style="left:113px">Contacts</h2>
  <p class="foot-text abs" style="left:113px">Contact us on 020 7946 0321</p>
  <div class="social abs" aria-label="Social links"><span></span><span></span><span></span><span></span></div>

  <h2 class="foot-title abs" style="left:373px">Link to our</h2>
  <p class="foot-text abs" style="left:374px">VIGIL platform</p>

  <div class="abs" style="left:605px;top:37px">
    <div class="brand"><span class="brand-mark"></span><span class="brand-name">QUORVANTA</span></div>
    <div class="brand-sub">Pharmacovigilance</div>
  </div>
  <p class="foot-text abs" style="left:608px;top:83px">Copyright © 2020 Quorvanta Ltd<br>(Registered in England &amp; Wales: 01234987)</p>
</footer>

</body>
</html>
```